Design A HVAC Business Website with Figma

We are launching a Web Design Service for HVAC and other Home Improvement businesses. We need to create some demo sites. These sites will be used to develop Webflow templates, so they must look very professional and real.

I am providing some sample data for this design. **,DO NOT USE LOREM IPSUM** anywhere in this design. We will be featuring these designs on our website and marketing materials.

More information can be found on this Notion page https://pallid-cove-q29.wikinest.example/Web-Design-Project-7d2a9e1f04b8c365a1e9d70f42c6b8e3

Industry/Entity Type

HVAC, Plumbing, Remodeling, General Contractor

Number of Pages Required

5+ page

Requirements
Must have
• Must be professional

```html
<!DOCTYPE html>
<html lang="en">
<head>
<meta charset="utf-8">
<title>Harborline HVAC</title>
<link href="https://fonts.googleapis.com/css2?family=Poppins:wght@400;500;600;700&display=swap" rel="stylesheet">
<style>
:root{
  --red:#e41b17;
  --red-dark:#c8130f;
  --yellow:#f0cf0a;
  --yellow-dark:#e2b90b;
  --ink:#1c1c1c;
  --text:#444;
  --muted:#666;
  --nav:#262626;
  --grey-bg:#efefef;
  --footer:#222;
  --white:#fff;
}
*{box-sizing:border-box;margin:0;padding:0}
html,body{width:1200px;height:4101px;overflow:hidden}
body{position:relative;font-family:"Poppins",sans-serif;color:var(--text);background:var(--white)}
.abs{position:absolute}
.btn{position:absolute;display:flex;align-items:center;justify-content:center;font-weight:600;font-size:11px;letter-spacing:.3px;text-transform:uppercase}
.btn-red{background:var(--red);color:var(--white)}
.btn-outline{border:1.5px solid var(--red);color:var(--red);background:var(--white)}
.btn-outline-y{border:1.5px solid var(--yellow);color:var(--ink);background:var(--white)}
.section-title{position:absolute;left:0;width:1200px;text-align:center;font-weight:700;font-size:36px;color:var(--ink);letter-spacing:.5px}
.title-bar{position:absolute;width:36px;height:3px;background:var(--yellow);left:582px}
.photo{position:absolute}

/* header */
.logo{font-weight:700;font-size:32px;color:var(--ink);letter-spacing:-.5px}
.topbar-info{font-size:11px;line-height:15px;color:var(--ink)}
.topbar-info strong{display:block;color:var(--red);font-size:14px;font-weight:700}
.nav{top:73px;left:0;width:1200px;height:37px;background:var(--nav)}
.nav ul{list-style:none;display:flex;position:absolute;left:110px;height:37px}
.nav li{color:var(--white);font-size:11.5px;font-weight:500;display:flex;align-items:center;justify-content:center;height:37px;text-transform:uppercase}
.nav li.active{background:var(--red)}

/* hero */
.hero{top:110px;left:0;width:1200px;height:557px;background:linear-gradient(90deg,#f3f3f3 0%,#e8e9ea 40%,#c9d6de 70%,#8aa2b4 100%)}
.hero h1{position:absolute;left:110px;top:162px;font-size:50px;line-height:52px;color:var(--ink);font-weight:700}
.hero h1 span{font-weight:400;display:block}
.hero p{position:absolute;left:110px;top:278px;width:460px;font-size:11.5px;line-height:19px;color:#333}

/* estimate band */
.band{top:667px;left:0;width:1200px;height:140px;background:var(--yellow)}
.input{position:absolute;top:75px;height:30px;background:var(--white);border:1px solid #ddd;font-size:10.5px;color:#555;padding:0 8px;display:flex;align-items:center}

/* about */
.body-text{font-size:11.6px;line-height:17.6px;color:#333}

/* services */
.card{position:absolute;top:1450px;width:230px;height:404px;background:var(--white)}
.card h3{position:absolute;top:208px;width:100%;text-align:center;font-size:14px;font-weight:700;color:var(--ink);line-height:17px}
.card p{position:absolute;left:28px;width:174px;text-align:center;font-size:10px;line-height:14px;color:var(--muted)}
.card .btn{left:58px;width:113px;height:32px;top:345px;font-size:10px}
.card-icon{position:absolute;top:147px;left:90px;width:50px;height:50px;border-radius:50%;border:3px solid var(--white);display:flex;align-items:center;justify-content:center}

/* why */
.why-icon{position:absolute;width:52px;height:52px;border-radius:50%;display:flex;align-items:center;justify-content:center;box-shadow:0 0 0 4px rgba(0,0,0,.04)}
.why-label{position:absolute;font-size:12.5px;font-weight:600;color:var(--ink);line-height:18px;letter-spacing:.3px;text-transform:uppercase}

/* testimonials */
.testi{top:2594px;left:0;width:1200px;height:458px;background:linear-gradient(135deg,#e02520,#d3140f)}
.quote-card{position:absolute;top:137px;width:334px;height:213px;background:var(--white)}
.quote-card p{position:absolute;left:25px;top:25px;width:290px;font-size:9.6px;line-height:13px;color:#444}
.quote-card .name{position:absolute;left:25px;top:180px;font-size:13px;font-weight:700;color:var(--ink)}
.stars{position:absolute;top:182px;color:var(--yellow);font-size:11px;letter-spacing:1px}
.avatar{position:absolute;width:38px;height:38px;border-radius:50%;border:2px solid var(--white)}
.arrow{position:absolute;width:32px;height:32px;border-radius:50%;background:var(--white);display:flex;align-items:center;justify-content:center}

/* footer */
.footer{top:3700px;left:0;width:1200px;height:401px;background:var(--footer)}
.foot-head{position:absolute;font-size:12.5px;font-weight:600;color:var(--white);text-transform:uppercase}
.foot-links{position:absolute;list-style:none;font-size:11.5px;line-height:23px;color:#cfcfcf}
.social{position:absolute;top:213px;width:32px;height:32px;border-radius:50%;border:1.5px solid #ccc;background:#2c2c2c}
.badge{position:absolute;top:3663px;width:62px;height:62px;border-radius:50%;background:rgba(255,255,255,.88);border:3px solid #f6d9d8}
.pay{position:absolute;top:4056px;width:30px;height:19px;border-radius:2px}
</style>
</head>
<body>

<!-- Header -->
<header>
  <div class="abs logo" style="left:108px;top:16px">HARBORLINE HVAC</div>
  <svg class="abs" style="left:697px;top:16px" width="42" height="42" viewBox="0 0 42 42" aria-hidden="true">
    <circle cx="21" cy="21" r="18" fill="none" stroke="var(--yellow)" stroke-width="3"/>
    <text x="21" y="25" text-anchor="middle" font-family="Poppins,sans-serif" font-size="10" font-weight="700" fill="var(--red)">24/7</text>
  </svg>
  <div class="abs topbar-info" style="left:746px;top:18px">It's 07:00 Am &amp; We're Open<strong>EMERGENCY SERVICE</strong></div>
  <svg class="abs" style="left:934px;top:18px" width="36" height="36" viewBox="0 0 24 24" aria-hidden="true">
    <path d="M6.6 10.8a15.1 15.1 0 0 0 6.6 6.6l2.2-2.2c.3-.3.7-.4 1-.2 1.1.4 2.3.6 3.6.6.6 0 1 .4 1 1V20c0 .6-.4 1-1 1A17 17 0 0 1 3 4c0-.6.4-1 1-1h3.5c.6 0 1 .4 1 1 0 1.3.2 2.5.6 3.6.1.3 0 .7-.2 1z" fill="var(--yellow-dark)"/>
  </svg>
  <div class="abs topbar-info" style="left:977px;top:18px;font-weight:700">CALL US TODAY!<strong>(555) 014-2790</strong></div>
</header>

<nav class="abs nav">
  <ul>
    <li class="active" style="width:97px">Home</li>
    <li style="width:106px">About Us</li>
    <li style="width:110px">Services</li>
    <li style="width:106px">Products</li>
    <li style="width:138px">Testimonials</li>
    <li style="width:98px">Gallery</li>
    <li style="width:128px">Contact Us</li>
    <li style="width:95px">Blog</li>
    <li style="width:78px">FAQ</li>
  </ul>
</nav>

<!-- Hero -->
<section class="abs hero">
  <div class="photo" role="img" aria-label="Technician fixing pipes under a kitchen sink" style="left:560px;top:0;width:640px;height:557px;background:linear-gradient(110deg,rgba(255,255,255,0) 0%,#b7c9d6 40%,#6f8fa6 100%)"></div>
  <h1>WELCOME TO<span>HARBORLINE HVAC</span></h1>
  <p>Your Trusted Source For Heating, Ventilation, And Air Conditioning Services In Bayview County. Our Team Of Certified Technicians Has Been Providing <strong>Top-notch Service To Our Customers For Over 13 Years.</strong></p>
  <div class="btn btn-red" style="left:110px;top:363px;width:143px;height:39px">Contact Us</div>
</section>

<!-- Estimate band -->
<section class="abs band">
  <svg class="abs" style="left:0;top:0" width="345" height="140" aria-hidden="true"><polygon points="0,0 305,0 345,70 305,140 0,140" fill="var(--yellow-dark)"/></svg>
  <div class="abs" style="left:113px;top:42px;font-size:22px;font-weight:700;color:var(--ink);letter-spacing:.5px">CALL US NOW!</div>
  <div class="abs" style="left:111px;top:66px;font-size:25px;font-weight:500;color:var(--red)">(555) 014-2790</div>
  <div class="abs" style="left:371px;top:35px;font-size:22px;font-weight:600;color:var(--ink)">GET YOUR ESTIMATE NOW!</div>
  <div class="input" style="left:376px;width:143px">Name:</div>
  <div class="input" style="left:525px;width:150px">Email:</div>
  <div class="input" style="left:681px;width:139px">Phone:</div>
  <div class="input" style="left:826px;width:131px;justify-content:space-between">Service For <span style="font-size:9px">&#8964;</span></div>
  <div class="btn btn-red" style="left:964px;top:75px;width:126px;height:30px">Submit Now</div>
</section>

<!-- About -->
<section>
  <svg class="abs" style="left:194px;top:998px" width="266" height="226" aria-hidden="true"><path d="M3 0 V223 H266" fill="none" stroke="var(--yellow)" stroke-width="6"/></svg>
  <div class="photo" role="img" aria-label="Smiling plumber in blue overalls repairing a sink" style="left:210px;top:874px;width:393px;height:336px;background:linear-gradient(135deg,#d9dcdf,#9aa9b6 60%,#3c5a86)"></div>
  <div class="abs" style="left:688px;top:864px;font-size:36px;font-weight:700;color:var(--ink)">ABOUT US</div>
  <div class="abs" style="left:688px;top:912px;width:36px;height:3px;background:var(--yellow)"></div>
  <p class="abs body-text" style="left:688px;top:934px;width:310px">Welcome To Harborline HVAC, Your Trusted Source For Heating, Ventilation, And Air Conditioning Services In Bayview County. Our Team Of Certified Technicians Has Been Providing Top-notch Service To Our Customers For Over 13 Years.</p>
  <p class="abs body-text" style="left:688px;top:1039px;width:310px">At Harborline HVAC, We Believe In Providing Personalized Service That Meets The Unique Needs Of Our Customers. We Know That HVAC Problems Can Be Stressful And Disruptive To Your Daily Routine, Which Is Why We Offer Flexible Scheduling And 24/7 Emergency Services To Ensure That We Are Always Available When You Need Us.</p>
  <div class="btn btn-red" style="left:688px;top:1184px;width:132px;height:40px">Lear More</div>
</section>

<!-- Services -->
<section class="abs" style="top:1289px;left:0;width:1200px;height:632px;background:var(--grey-bg)"></section>
<h2 class="section-title" style="top:1362px">OUR SERVICES</h2>
<div class="title-bar" style="top:1410px"></div>

<article class="card" style="left:110px">
  <div class="photo" role="img" aria-label="Technician servicing a furnace" style="left:0;top:0;width:230px;height:173px;background:linear-gradient(135deg,#c9ccd0,#8d3a34 60%,#4a4f58)"></div>
  <div class="card-icon" style="background:var(--yellow)"><svg width="22" height="22" viewBox="0 0 22 22" aria-hidden="true"><rect x="3" y="7" width="16" height="10" rx="1" fill="none" stroke="#fff" stroke-width="2"/><path d="M7 7v10M11 7v10M15 7v10" stroke="#fff" stroke-width="2"/></svg></div>
  <h3>HEATING SERVICES</h3>
  <p style="top:254px">Whether You Need A New Furnace Installed, An Old System Repaired, Or Routine Maintenance, Our Team Has The Expertise To Keep You Warm And Cozy All Winter Long.</p>
  <div class="btn btn-outline-y">Lear More</div>
</article>

<article class="card" style="left:360px">
  <div class="photo" role="img" aria-label="Technician in hard hat working on an outdoor air conditioner" style="left:0;top:0;width:230px;height:173px;background:linear-gradient(135deg,#eef0f2,#b8bec4 50%,#c99a3a)"></div>
  <div class="card-icon" style="background:var(--red)"><svg width="22" height="22" viewBox="0 0 22 22" aria-hidden="true"><rect x="3" y="5" width="16" height="7" rx="1.5" fill="none" stroke="#fff" stroke-width="2"/><path d="M7 15v3M11 15v3M15 15v3" stroke="#fff" stroke-width="2"/></svg></div>
  <h3>AIR CONDITIONING<br>SERVICES</h3>
  <p style="top:271px">Stay Cool And Comfortable All Summer Long With Our Expert Air Conditioning Services. We Offer Installation, Repair, And Maintenance Services For All Types Of AC Units.</p>
  <div class="btn btn-red" style="left:58px;width:113px;height:32px;top:345px;font-size:10px">Lear More</div>
</article>

<article class="card" style="left:610px">
  <div class="photo" role="img" aria-label="Bright modern open office interior" style="left:0;top:0;width:230px;height:173px;background:linear-gradient(135deg,#e7eaec,#a9b6b3 55%,#6f8c6a)"></div>
  <div class="card-icon" style="background:var(--yellow)"><svg width="22" height="22" viewBox="0 0 22 22" aria-hidden="true"><path d="M3 11 11 4l8 7v8H3z" fill="none" stroke="#fff" stroke-width="2"/><path d="M8 14h6" stroke="#fff" stroke-width="2"/></svg></div>
  <h3>INDOOR AIR QUALITY</h3>
  <p style="top:254px">We Know That Indoor Air Quality Is Essential For Your Health And Comfort. Our Team Can Help You Improve Your Indoor Air Quality By Installing Air Purifiers, Humidifiers, And Ventilation Systems.</p>
  <div class="btn btn-outline-y">Lear More</div>
</article>

<article class="card" style="left:859px">
  <div class="photo" role="img" aria-label="Engineers inspecting ductwork in a commercial building" style="left:0;top:0;width:231px;height:173px;background:linear-gradient(135deg,#f1f2f3,#c9ced3 55%,#8fa0ac)"></div>
  <div class="card-icon" style="background:var(--yellow)"><svg width="22" height="22" viewBox="0 0 22 22" aria-hidden="true"><path d="M3 19V9h5v10M9 19V5h6v14M16 19v-7h3v7" fill="none" stroke="#fff" stroke-width="2"/></svg></div>
  <h3>COMMERCIAL HVAC</h3>
  <p style="top:254px">Our Commercial HVAC Services Are Designed To Keep Your Business Running Smoothly. From Routine Maintenance To Complex Installations, Our Team Can Handle It All.</p>
  <div class="btn btn-outline-y">Lear More</div>
</article>

<!-- Why choose -->
<h2 class="section-title" style="top:1976px">WHY CHOOSE HARBORLINE HVAC?</h2>
<div class="title-bar" style="top:2024px"></div>
<svg class="abs" style="left:400px;top:2035px" width="400" height="400" aria-hidden="true"><circle cx="200" cy="200" r="172" fill="none" stroke="#bbb" stroke-width="1.2" stroke-dasharray="2 4"/></svg>
<div class="photo" role="img" aria-label="Smiling technician in blue uniform giving a thumbs up" style="left:487px;top:2122px;width:226px;height:226px;border-radius:50%;background:radial-gradient(circle at 50% 40%,#cfd6de,#2f4f9a 70%)"></div>

<div class="why-icon" style="left:480px;top:2060px;background:var(--red)"><svg width="22" height="22" viewBox="0 0 22 22" aria-hidden="true"><path d="M4 11l5 5 9-10" fill="none" stroke="#fff" stroke-width="2.5"/></svg></div>
<div class="why-label" style="left:300px;top:2067px;width:164px;text-align:right">Satisfaction<br>Guarantee</div>

<div class="why-icon" style="left:668px;top:2060px;background:var(--red)"><svg width="22" height="22" viewBox="0 0 22 22" aria-hidden="true"><circle cx="11" cy="9" r="6" fill="none" stroke="#fff" stroke-width="2"/><path d="M7 14l-2 6 6-3 6 3-2-6" fill="none" stroke="#fff" stroke-width="2"/></svg></div>
<div class="why-label" style="left:737px;top:2067px">Experienced And<br>Certified Technicians</div>

<div class="why-icon" style="left:401px;top:2186px;background:var(--yellow)"><svg width="22" height="22" viewBox="0 0 22 22" aria-hidden="true"><circle cx="11" cy="11" r="4" fill="none" stroke="#fff" stroke-width="2"/><path d="M11 2v4M11 16v4M2 11h4M16 11h4" stroke="#fff" stroke-width="2"/></svg></div>
<div class="why-label" style="left:220px;top:2193px;width:166px;text-align:right">Personalized<br>Service</div>

<div class="why-icon" style="left:748px;top:2186px;background:var(--yellow)"><svg width="22" height="22" viewBox="0 0 22 22" aria-hidden="true"><circle cx="11" cy="11" r="8" fill="none" stroke="#fff" stroke-width="2"/><path d="M11 6v5l3 2" fill="none" stroke="#fff" stroke-width="2"/></svg></div>
<div class="why-label" style="left:817px;top:2193px">24/7 Emergency<br>Services</div>

<div class="why-icon" style="left:439px;top:2310px;background:var(--red)"><svg width="22" height="22" viewBox="0 0 22 22" aria-hidden="true"><path d="M5 17 14 8M13 4l5 5-3 1-3-3z" fill="none" stroke="#fff" stroke-width="2"/></svg></div>
<div class="why-label" style="left:240px;top:2315px;width:184px;text-align:right">High-Quality<br>Equipment And Parts</div>

<div class="why-icon" style="left:709px;top:2310px;background:var(--red)"><svg width="22" height="22" viewBox="0 0 22 22" aria-hidden="true"><rect x="3" y="5" width="16" height="14" rx="1.5" fill="none" stroke="#fff" stroke-width="2"/><path d="M3 9h16M7 3v4M15 3v4M8 14l2 2 4-4" fill="none" stroke="#fff" stroke-width="2"/></svg></div>
<div class="why-label" style="left:780px;top:2315px">Flexible<br>Scheduling</div>

<div class="why-icon" style="left:574px;top:2374px;background:var(--yellow)"><svg width="22" height="22" viewBox="0 0 22 22" aria-hidden="true"><circle cx="11" cy="11" r="7" fill="none" stroke="#fff" stroke-width="2"/><text x="11" y="15" text-anchor="middle" font-family="Poppins,sans-serif" font-size="10" font-weight="700" fill="#fff">$</text></svg></div>
<div class="why-label" style="left:0;width:1200px;text-align:center;top:2442px">Upfront Pricing</div>

<div class="btn btn-outline" style="left:506px;top:2488px;width:186px;height:38px;font-size:11.5px">Get Estimate Now</div>

<!-- Testimonials -->
<section class="abs testi">
  <h2 class="section-title" style="top:54px;color:var(--white)">TESTIMONIALS</h2>
  <div class="title-bar" style="top:102px"></div>

  <div class="avatar" role="img" aria-label="Customer portrait" style="left:158px;top:161px;background:#c99a7e"></div>
  <div class="quote-card" style="left:218px">
    <p>I Had An Amazing Experience With Harborline HVAC. They Quickly Responded To My Call And Scheduled A Technician To Come Out To My Home Within Hours. The Technician Was Professional, Knowledgeable, And Friendly. He Quickly Diagnosed And Repaired My Air Conditioning Unit And Made Sure To Clean Up After Himself Before Leaving. I Couldn't Be Happier With The Service I Received And Highly Recommend Harborline HVAC To Anyone In Need Of HVAC Services. Thank You For The Exceptional Work!</p>
    <div class="name">MARLA DENNISON</div>
    <div class="stars" style="left:148px">&#9733;&#9733;&#9733;&#9733;&#9733;</div>
    <div class="abs" style="right:22px;top:165px;font-size:52px;line-height:52px;color:#ddd;font-weight:700">&rdquo;</div>
  </div>

  <div class="avatar" role="img" aria-label="Customer portrait" style="left:586px;top:161px;background:#7d8ea4"></div>
  <div class="quote-card" style="left:646px">
    <p>I Recently Had Harborline HVAC Replace My Central Heating Unit, And I Was Extremely Impressed With Their Service. They Provided A Thorough Assessment Of My Needs And Recommended A High-quality Replacement System That Fit My Budget. The Installation Process Was Quick And Efficient, And The Team Was Very Professional Throughout. My New Heating Unit Is Working Perfectly, And I Couldn't Be Happier With The Results. I Would Highly Recommend Harborline HVAC To Anyone In Need Of HVAC Services. Thank You For The Excellent Work!</p>
    <div class="name" style="left:46px">TOBIAS GREER</div>
    <div class="stars" style="left:168px">&#9733;&#9733;&#9733;&#9733;&#9733;</div>
    <div class="abs" style="right:22px;top:165px;font-size:52px;line-height:52px;color:#ddd;font-weight:700">&rdquo;</div>
  </div>

  <div class="arrow" style="left:151px;top:226px"><svg width="12" height="12" viewBox="0 0 12 12" aria-hidden="true"><path d="M8 2 4 6l4 4" fill="none" stroke="#333" stroke-width="1.6"/></svg></div>
  <div class="arrow" style="left:1015px;top:226px"><svg width="12" height="12" viewBox="0 0 12 12" aria-hidden="true"><path d="M4 2l4 4-4 4" fill="none" stroke="#333" stroke-width="1.6"/></svg></div>

  <svg class="abs" style="left:562px;top:376px" width="76" height="16" aria-hidden="true">
    <circle cx="8" cy="8" r="4" fill="none" stroke="#fff" stroke-width="1.2"/>
    <circle cx="28" cy="8" r="6" fill="var(--yellow)"/>
    <circle cx="48" cy="8" r="4" fill="none" stroke="#fff" stroke-width="1.2"/>
    <circle cx="66" cy="8" r="4" fill="none" stroke="#fff" stroke-width="1.2"/>
  </svg>
</section>

<!-- Gallery -->
<h2 class="section-title" style="top:3106px">WORK <span style="border-bottom:0">GALLERY</span></h2>
<div class="abs" style="left:582px;top:3155px;width:36px;height:3px;background:var(--yellow)"></div>
<div class="photo" role="img" aria-label="Dated shower stall before remodel" style="left:110px;top:3190px;width:234px;height:323px;background:linear-gradient(160deg,#b9b9b9,#8a8a8a)"></div>
<div class="photo" role="img" aria-label="Bathroom with yellow curtain before remodel" style="left:363px;top:3190px;width:234px;height:323px;background:linear-gradient(160deg,#e5c34b,#b8952c)"></div>
<div class="photo" role="img" aria-label="Remodeled white tiled tub surround" style="left:603px;top:3190px;width:234px;height:323px;background:linear-gradient(160deg,#f1f1f1,#d2d2d2)"></div>
<div class="photo" role="img" aria-label="Finished shower remodel" style="left:856px;top:3190px;width:234px;height:323px;background:linear-gradient(160deg,#cfcfcf,#9d9d9d)"></div>
<div class="abs" style="left:375px;top:3488px;font-size:13px;color:#fff;font-weight:500">BEFORE</div>
<div class="abs" style="left:782px;top:3488px;font-size:13px;color:#fff;font-weight:500">AFTER</div>
<div class="abs" style="left:572px;top:3325px;width:56px;height:56px;border-radius:50%;background:#fff;display:flex;align-items:center;justify-content:center"><svg width="24" height="14" viewBox="0 0 24 14" aria-hidden="true"><path d="M9 1 3 7l6 6zM15 1l6 6-6 6z" fill="#999"/></svg></div>
<div class="btn btn-outline" style="left:511px;top:3547px;width:178px;height:40px;font-size:11.5px">View More Works</div>

<!-- Footer -->
<footer class="abs footer">
  <div class="abs logo" style="left:208px;top:165px;color:var(--white);font-size:30px">HARBORLINE HVAC</div>
  <div class="social" style="left:254px"></div>
  <div class="social" style="left:294px"></div>
  <div class="social" style="left:334px"></div>
  <div class="social" style="left:374px"></div>

  <div class="foot-head" style="left:533px;top:127px">Quick Links</div>
  <ul class="foot-links" style="left:533px;top:160px"><li>Home</li><li>About Us</li><li>Services</li><li>Products</li><li>Faq</li></ul>
  <div class="foot-head" style="left:659px;top:127px">More Links</div>
  <ul class="foot-links" style="left:659px;top:160px"><li>Gallery</li><li>Contact Us</li><li>Blog</li><li>Testimonials</li></ul>
  <div class="foot-head" style="left:807px;top:127px">Follow Us</div>

  <svg class="abs" style="left:808px;top:164px" width="14" height="18" viewBox="0 0 14 18" aria-hidden="true"><path d="M7 1a6 6 0 0 0-6 6c0 4.5 6 10 6 10s6-5.5 6-10a6 6 0 0 0-6-6z" fill="none" stroke="var(--yellow)" stroke-width="1.8"/><circle cx="7" cy="7" r="2" fill="var(--yellow)"/></svg>
  <div class="abs" style="left:832px;top:161px;font-size:11.5px;line-height:17px;color:#ddd">4820 Corvina Harbor Rd,<br>Bayview, CA 90000</div>
  <svg class="abs" style="left:808px;top:222px" width="15" height="15" viewBox="0 0 24 24" aria-hidden="true"><path d="M6.6 10.8a15.1 15.1 0 0 0 6.6 6.6l2.2-2.2c.3-.3.7-.4 1-.2 1.1.4 2.3.6 3.6.6.6 0 1 .4 1 1V20c0 .6-.4 1-1 1A17 17 0 0 1 3 4c0-.6.4-1 1-1h3.5c.6 0 1 .4 1 1 0 1.3.2 2.5.6 3.6.1.3 0 .7-.2 1z" fill="var(--yellow)"/></svg>
  <div class="abs" style="left:832px;top:217px;font-size:15px;font-weight:600;color:var(--white)">1-555-019-3384</div>
  <svg class="abs" style="left:808px;top:267px" width="15" height="12" viewBox="0 0 15 12" aria-hidden="true"><rect x="0.5" y="0.5" width="14" height="11" rx="1" fill="var(--yellow)"/><path d="M1 1l6.5 5L14 1" fill="none" stroke="#222" stroke-width="1.2"/></svg>
  <div class="abs" style="left:832px;top:264px;font-size:11.5px;color:#ddd">hello@harborlinehvac.example</div>

  <div class="abs" style="left:0;top:342px;width:1200px;height:1px;background:#3a3a3a"></div>
  <div class="abs" style="left:210px;top:358px;font-size:10px;color:#ddd;font-weight:500">©2023 HARBORLINE HVAC. ALL RIGHTS RESERVED.</div>
  <div class="abs" style="left:777px;top:358px;font-size:10px;color:#aaa">We Accept:</div>
</footer>
<div class="pay" style="left:847px;background:#5a6a86"></div>
<div class="pay" style="left:883px;background:#2d4b8e"></div>
<div class="pay" style="left:919px;background:#4d8fd6"></div>
<div class="pay" style="left:955px;background:#d9d9d9"></div>

<!-- Ribbon with badges -->
<svg class="abs" style="left:143px;top:3645px" width="912" height="100" aria-hidden="true">
  <polygon points="0,18 51,18 51,98 0,98 22,58" fill="var(--red-dark)"/>
  <polygon points="912,18 861,18 861,98 912,98 890,58" fill="var(--red-dark)"/>
  <rect x="51" y="0" width="810" height="98" fill="var(--red)"/>
</svg>
<div class="badge" style="left:243px;border-radius:8px"></div>
<div class="badge" style="left:350px;border-radius:8px;width:50px"></div>
<div class="badge" style="left:510px;width:80px;border-radius:6px;background:rgba(255,255,255,.75)"></div>
<div class="badge" style="left:653px;border-radius:8px"></div>
<div class="badge" style="left:771px"></div>
<div class="badge" style="left:891px;border-radius:8px;width:56px"></div>

</body>
</html>
```